Velvet Pressings Techno Label Business Card

I'm looking for a very clean business card for my Velvet Pressings music label. The label focusses on techno music. The card should include:

• my name : Bram Quintel as "Founder & CEO"
• email address: bram@velvet-pressings.example
• web: www.velvet-pressings.example
• facebook logo + /velvetpress
• twitter logo + /velvetpress
• soundcloud logo + /velvetpressings

Feel free to include your ideas! I'm looking forward to discuss about it.

Bram

Industry/Entity Type

Business

Contact Information for Business Card

I don't like glossy cards. Prefer matt.

Requirements
Nice to have
• Maybe on one side the complete logo, other side just the icon.
Should not have
• Flashy stuff. Must be clean and business like style.

```html
<!DOCTYPE html>
<html lang="en">
<head>
<meta charset="utf-8">
<title>Velvet Pressings – Business Card</title>
<link rel="stylesheet" href="https://fonts.googleapis.com/css2?family=Open+Sans:wght@400;600;700&display=swap">
<style>
  :root {
    --bg: #e9e7e4;
    --card: #ffffff;
    --grey: #7a7a7a;
    --grey-text: #555555;
    --orange: #f26a12;
    --peach: #fbd7bf;
  }
  * { margin: 0; padding: 0; box-sizing: border-box; }
  html, body { width: 1200px; height: 800px; overflow: hidden; }
  body {
    background: var(--bg);
    font-family: "Open Sans", Arial, sans-serif;
    position: relative;
  }
  .card {
    position: absolute;
    top: 257px;
    width: 500px;
    height: 286px;
    background: var(--card);
    box-shadow: 0 6px 18px rgba(0,0,0,0.12);
    overflow: hidden;
  }
  .card--front { left: 70px; }
  .card--back { left: 630px; }

  .front-waves { position: absolute; inset: 0; width: 100%; height: 100%; }

  .contact-list {
    position: absolute;
    left: 26px;
    top: 80px;
    list-style: none;
    font-size: 10.5px;
    color: var(--grey-text);
  }
  .contact-list li {
    display: flex;
    align-items: center;
    gap: 9px;
    height: 16px;
    white-space: nowrap;
  }
  .contact-list svg { width: 11px; height: 11px; flex: none; }
  .social-dot {
    width: 10px; height: 10px;
    border-radius: 50%;
    background: var(--orange);
    flex: none;
    margin: 0 0.5px;
  }

  .identity {
    position: absolute;
    left: 210px;
    top: 214px;
  }
  .wordmark {
    display: flex;
    align-items: center;
    gap: 7px;
    font-weight: 700;
    font-size: 18px;
    line-height: 24px;
    letter-spacing: -0.4px;
    color: var(--orange);
    margin-bottom: 4px;
    white-space: nowrap;
  }
  .wordmark-dot {
    width: 12px; height: 12px;
    border-radius: 50%;
    background: var(--orange);
    flex: none;
  }
  .person-name {
    font-weight: 700;
    font-size: 14px;
    line-height: 18px;
    color: var(--orange);
    text-transform: uppercase;
    letter-spacing: 0.5px;
  }
  .person-role {
    font-size: 11px;
    line-height: 15px;
    color: var(--grey-text);
  }

  .back-disc {
    position: absolute;
    left: 40px;
    top: -70px;
    width: 200px;
    height: 200px;
    border-radius: 50%;
    background: var(--peach);
  }
  .back-wordmark {
    position: absolute;
    left: 40px;
    bottom: 60px;
    font-weight: 700;
    font-size: 32px;
    letter-spacing: -0.8px;
    color: var(--orange);
  }
</style>
</head>
<body>

  <section class="card card--front" aria-label="Business card front">
    <svg class="front-waves" viewBox="0 0 500 286" aria-hidden="true">
      <path d="M0,0 H500 V286 H470 C430,200 380,80 0,30 Z" fill="var(--grey)"/>
      <path d="M0,56 C140,28 270,58 338,150 C262,80 140,54 0,72 Z" fill="var(--orange)"/>
    </svg>

    <ul class="contact-list">
      <li>
        <svg viewBox="0 0 12 12"><rect x="3" y="0.5" width="6" height="11" rx="1.2" fill="none" stroke="var(--orange)" stroke-width="1.3"/></svg>
        012 555 0148
      </li>
      <li>
        <svg viewBox="0 0 12 12"><path d="M2.5,1 L5,1 L5.8,3.8 L4.4,5 C5,6.6 5.6,7.2 7,7.8 L8.2,6.4 L11,7.2 L11,9.6 C11,10.6 10,11 9,11 C4.5,10.5 1.5,7.5 1,3 C1,2 1.5,1 2.5,1 Z" fill="var(--orange)"/></svg>
        012 555 0172
      </li>
      <li>
        <svg viewBox="0 0 12 12"><rect x="0.5" y="2" width="11" height="8" rx="1" fill="var(--orange)"/><path d="M1,2.6 L6,6.6 L11,2.6" fill="none" stroke="#fff" stroke-width="1"/></svg>
        bram@velvet-pressings.example
      </li>
      <li>
        <svg viewBox="0 0 12 12"><circle cx="6" cy="6" r="5.5" fill="var(--orange)"/><path d="M0.5,6 H11.5 M6,0.5 C3,3.5 3,8.5 6,11.5 M6,0.5 C9,3.5 9,8.5 6,11.5" fill="none" stroke="#fff" stroke-width="0.8"/></svg>
        www.velvet-pressings.example
      </li>
      <li><span class="social-dot"></span>/velvetpress</li>
      <li><span class="social-dot"></span>/velvetpress</li>
      <li><span class="social-dot"></span>/velvetpressings</li>
      <li>
        <svg viewBox="0 0 12 12"><path d="M6,11.5 C3,8 2,6 2,4.3 C2,2 3.8,0.5 6,0.5 C8.2,0.5 10,2 10,4.3 C10,6 9,8 6,11.5 Z" fill="var(--orange)"/><circle cx="6" cy="4.3" r="1.5" fill="#fff"/></svg>
        14 Kiln Lane, Floor 3, Harbour Road
      </li>
    </ul>

    <div class="identity">
      <div class="wordmark"><span class="wordmark-dot"></span>Velvet Pressings</div>
      <p class="person-name">Bram Quintel</p>
      <p class="person-role">Founder &amp; CEO</p>
    </div>
  </section>

  <section class="card card--back" aria-label="Business card back">
    <div class="back-disc"></div>
    <p class="back-wordmark">Velvet Pressings</p>
  </section>

</body>
</html>
```